依頼概要
■ 依頼の目的/概要

当社は、「モフルナ」というサイトで似顔絵の売買仲介サービスをご提供しています。リニューアルに伴い、トップページデザイン(コーディング無し)を募集させて頂きます。

考慮していただきたい点は以下の通りです。
・似顔絵サイトなので商品画像が映えるようなデザイン
・基本的な構成は現在のサイトと同じ(横幅950px、2カラム)
・ヘッダーと右カラムはどのページでも共通に表示
・右カラムは、デザインを崩さない程度にできるだけ狭く表示
・「モフルナ」というロゴのデザインもお願いします
・コンテンツは現状のものでも大幅に変えていただいても構いません(可能ならば他ページのコンテンツも見て新たに考えていただければと思います)
・選ばせていただいた方には、他ページにも汎用的に使える見出しタグ(h1,h2,h3)のデザインもお願いします
・作成頂いたウェブサイトをベースに他ページも制作したい(追加料金を払ってお願いする可能性もあります)

・現在のウェブサイト
http://mofuruna.example.jp/

■ 納品ファイルの希望

Illustrator、Photoshop、 InkScape、Gimp形式のいづれか

■ その他/注意点

選択させて頂いたウェブデザインの著作権(財産権)等の扱いはWrittel利用規約に従い、弊社に譲渡をお願いします。フォントや画像素材などを利用する場合は上記利用用途に使用できることを確認し、第三者の知的財産権等に注意して下さい。
■ 選んだ理由

コンセプトが一番はっきりしており、デザインもまとまりがあるように感じました。
現在のデザインから、ガラッとイメージが変わったのも良かったです。

パーツで見ると他の方の作品も素晴らしいのですが、まとまりを重視させていただきました。

■ 提案者全員のお礼・コメント

予想以上に多くの方、素晴らしいデザインをご提供していただきまして、ありがとうございました。

```html
<!DOCTYPE html>
<html lang="ja">
<head>
<meta charset="utf-8">
<title>モフルナ｜似顔絵師のための売買仲介サイト</title>
<link href="https://fonts.googleapis.com/css2?family=Noto+Sans+JP:wght@400;500;700&family=M+PLUS+Rounded+1c:wght@400;500;700&display=swap" rel="stylesheet">
<style>
:root{
  --blue:#1e73b8;
  --blue-dark:#0d5aa8;
  --link:#2a6fc0;
  --gray-bar:#d4d4d4;
  --gray-btn:#9a9a9a;
  --gray-head:#d9d9d9;
  --text:#222;
  --sub:#666;
  --pink:#e0189a;
  --orange:#f08a1c;
  --green:#3ac24a;
  --red:#e02030;
  --magenta:#d62ba0;
  --white:#fff;
}
*{box-sizing:border-box;margin:0;padding:0}
html,body{width:1091px;height:1200px;overflow:hidden;background:var(--white)}
body{position:relative;font-family:"Noto Sans JP",sans-serif;color:var(--text)}
a{color:inherit;text-decoration:none}
.abs{position:absolute}

.top-rule{left:20px;top:0;width:1055px;height:9px;background:var(--gray-bar)}
.util{right:16px;top:11px;display:flex;gap:7px}
.util a{display:block;background:var(--gray-btn);color:var(--white);font-size:13px;padding:3px 0;text-align:center;width:92px}
.logo{left:82px;top:22px;font-family:"M PLUS Rounded 1c",sans-serif;font-weight:700;font-size:46px;color:var(--blue);letter-spacing:1px;line-height:1}
.tagline{left:308px;top:44px;font-size:13px;font-weight:500}

.gnav{left:82px;top:100px;display:flex;gap:34px;font-size:17px;color:#555;font-family:"M PLUS Rounded 1c",sans-serif}
.gnav li{list-style:none;display:flex;align-items:center;gap:6px}
.gnav svg{width:17px;height:17px}

.hero-photo{left:55px;top:149px;width:314px;height:276px;background:linear-gradient(160deg,#f2efe9,#e8e2da 60%,#dcd3c8)}
.hero-title{left:470px;top:188px;font-family:"M PLUS Rounded 1c",sans-serif;font-size:29px;font-weight:700;color:var(--blue)}
.uses{left:400px;top:249px;display:flex;gap:6px}
.uses li{list-style:none;width:90px;height:90px;border-radius:50%;border:2px solid;display:flex;align-items:center;justify-content:center;text-align:center;font-size:18px;line-height:1.2;font-family:"M PLUS Rounded 1c",sans-serif}
.u1{border-color:var(--blue)!important}.u2{border-color:var(--orange)!important}.u3{border-color:var(--magenta)!important}.u4{border-color:var(--green)!important}.u5{border-color:var(--red)!important}
.gift{left:412px;top:366px;color:var(--pink);font-size:17px;line-height:1.45;font-family:"M PLUS Rounded 1c",sans-serif;font-weight:500}
.cta{left:670px;top:371px;width:216px;height:47px;border-radius:9px;background:linear-gradient(#3d8fe0,var(--blue-dark));color:var(--white);font-size:18px;display:flex;align-items:center;justify-content:center;gap:8px;font-family:"M PLUS Rounded 1c",sans-serif;font-weight:500}

.sec-head{left:20px;width:866px;height:34px;background:var(--gray-head);display:flex;align-items:center;justify-content:space-between;padding:0 14px 0 24px}
.sec-head h2{font-size:18px;font-weight:500}
.sec-head h2 small{color:var(--white);font-size:13px;margin-right:6px;font-weight:400}
.sec-head .en{color:var(--white);font-size:27px;font-family:"Noto Sans JP",sans-serif;letter-spacing:.5px}

.cards{left:36px;display:flex;gap:14px}
.card{list-style:none;width:155px;text-align:center}
.card .art{height:155px}
.card a{display:block;margin-top:8px;color:var(--link);text-decoration:underline;font-size:15px}
.y{background:#f7ef6a}.bw{background:linear-gradient(135deg,#e7e1d3,#3a3530)}.pk{background:radial-gradient(ellipse at center,#e8569b 45%,#fff 47%)}.sp{background:linear-gradient(#f5ede1,#d9c2a8)}.yl{background:#f9f07c}

.news{left:50px;top:1030px;font-size:13px;color:var(--link);line-height:23px}
.news li{list-style:none;display:flex}
.news time{width:115px}

.foot-rule{left:20px;top:1129px;width:1055px;height:8px;background:var(--gray-bar)}
.foot-links{left:0;width:1091px;top:1148px;text-align:center;font-size:13px}
.copy{left:0;width:1091px;top:1175px;text-align:center;font-size:12px}

.side{left:901px;width:174px}
.side-head{background:var(--gray-head);height:26px;text-align:center;font-size:15px;font-weight:700;line-height:26px}
.pill{display:block;margin:0 auto;width:118px;height:25px;border-radius:6px;background:linear-gradient(#3d8fe0,var(--blue-dark));color:var(--white);font-size:14px;text-align:center;line-height:25px}
.reg{display:flex;align-items:center;gap:12px;padding:6px 0 10px 18px;color:var(--sub);font-size:15px;line-height:1.25}
.reg .ico{width:46px;height:40px}
.search{font-size:12px}
.search .row{display:flex;align-items:center;margin:0 0 8px 6px}
.search .row>span{width:68px;font-weight:500}
.sel{width:88px;height:16px;border:1px solid #999;font-size:11px;display:flex;justify-content:space-between;align-items:center;padding-left:3px}
.sel::after{content:"▼";font-size:8px;border-left:1px solid #999;width:14px;text-align:center}
.chk{display:flex;gap:4px;font-size:12px;color:#444}
.chk i{display:inline-block;width:11px;height:11px;border:1px solid #999;margin-right:2px;vertical-align:-1px}
.sbtn{display:block;margin:8px 18px 0 auto;width:70px;height:21px;border-radius:5px;background:linear-gradient(#3d8fe0,var(--blue-dark));color:var(--white);font-size:13px;text-align:center;line-height:21px}
.goods{border:1px solid #ccc;border-top:none}
.goods li{list-style:none;height:46px;border-top:1px solid #ccc;display:flex;align-items:center;gap:14px;padding-left:12px;font-size:15px}
.goods li .thumb{width:26px;height:24px;border:1px solid #ccc;background:#f1f1f1}
.goods li.other{justify-content:center;padding-left:0}
</style>
</head>
<body>

<div class="abs top-rule"></div>
<nav class="abs util"><a href="#">カートを見る</a><a href="#">マイページ</a><a href="#">ログイン</a></nav>
<div class="abs logo">mofuruna</div>
<p class="abs tagline">似顔絵師のための売買仲介サイト</p>

<ul class="abs gnav">
  <li><svg viewBox="0 0 20 20"><circle cx="10" cy="10" r="9" fill="#36a6df"/><path d="M5 11l5-5 5 5v4H5z" fill="#fff"/></svg>トップ</li>
  <li><svg viewBox="0 0 20 20"><circle cx="10" cy="10" r="9" fill="#36a6df"/><path d="M10 4l1.8 4h4l-3.2 2.5 1.2 4L10 12l-3.8 2.5 1.2-4L4.2 8h4z" fill="#fff"/></svg>クリエイターを見る</li>
  <li><svg viewBox="0 0 20 20"><circle cx="10" cy="10" r="9" fill="#36a6df"/><path d="M10 4l1.8 4h4l-3.2 2.5 1.2 4L10 12l-3.8 2.5 1.2-4L4.2 8h4z" fill="#fff"/></svg>商品を見る</li>
  <li><svg viewBox="0 0 20 20"><circle cx="10" cy="10" r="9" fill="#36a6df"/><text x="10" y="14.5" font-size="12" text-anchor="middle" fill="#fff" font-family="sans-serif" font-weight="700">?</text></svg>モフルナとは</li>
  <li><svg viewBox="0 0 20 20"><circle cx="10" cy="10" r="9" fill="#36a6df"/><circle cx="10" cy="8" r="3" fill="#fff"/><path d="M5 15a5 4 0 0110 0z" fill="#fff"/></svg>会員登録</li>
  <li><svg viewBox="0 0 20 20"><circle cx="10" cy="10" r="9" fill="#36a6df"/><rect x="5" y="6.5" width="10" height="7" fill="#fff"/><path d="M5 6.5l5 4 5-4" stroke="#36a6df" fill="none"/></svg>お問い合わせ</li>
</ul>

<div class="abs hero-photo" role="img" aria-label="サイト名を書いたボードを持つ女性の写真"></div>
<h1 class="abs hero-title">使い方はあなた次第♪</h1>
<ul class="abs uses">
  <li class="u1">mimo</li><li class="u2">プロフ<br>画像</li><li class="u3">名刺</li><li class="u4">パンフ<br>レット</li><li class="u5" style="font-size:16px">ウェルカム<br>ボード</li>
</ul>
<p class="abs gift">プレゼントにもぴったり!<br>宝物を届けます。</p>
<a class="abs cta" href="#"><svg width="12" height="14" viewBox="0 0 12 14"><path d="M2 1l8 6-8 6z" fill="#fff"/></svg>クリエイターを見る</a>

<header class="abs sec-head" style="top:467px"><h2>注目クリエイター</h2><span class="en">Pick up</span></header>
<ul class="abs cards" style="top:527px">
  <li class="card"><div class="art y" role="img" aria-label="クリエイターhinaの似顔絵作品"></div><a href="#">hina</a></li>
  <li class="card"><div class="art bw" role="img" aria-label="クリエイターTAKKUN.のモノクロイラスト作品"></div><a href="#">TAKKUN.</a></li>
  <li class="card"><div class="art pk" role="img" aria-label="クリエイターぽっぽの似顔絵作品"></div><a href="#">ぽっぽ</a></li>
  <li class="card"><div class="art sp" role="img" aria-label="クリエイターKAEDEの似顔絵作品"></div><a href="#" style="text-decoration:none">KAEDE</a></li>
  <li class="card"><div class="art yl" role="img" aria-label="クリエイターエムティの似顔絵作品"></div><a href="#">エムティ</a></li>
</ul>

<header class="abs sec-head" style="top:724px"><h2><small>NEW</small>新着クリエイター</h2><span class="en">Creators</span></header>
<ul class="abs cards" style="top:780px">
  <li class="card"><div class="art pk" role="img" aria-label="クリエイターぽっぽの似顔絵作品"></div><a href="#">ぽっぽ</a></li>
  <li class="card"><div class="art sp" role="img" aria-label="クリエイターKAEDEの似顔絵作品"></div><a href="#" style="text-decoration:none">KAEDE</a></li>
  <li class="card"><div class="art yl" role="img" aria-label="クリエイターエムティの似顔絵作品"></div><a href="#">エムティ</a></li>
  <li class="card"><div class="art y" role="img" aria-label="クリエイターhinaの似顔絵作品"></div><a href="#">hina</a></li>
  <li class="card"><div class="art bw" role="img" aria-label="クリエイターTAKKUN.のモノクロイラスト作品"></div><a href="#">TAKKUN.</a></li>
</ul>

<header class="abs sec-head" style="top:980px"><h2>お知らせ</h2><span class="en">News topic</span></header>
<ul class="abs news">
  <li><time>2011.02.19.</time>モフルナオープン　 似顔絵売買仲介の「モフルナ」がオープンしました。</li>
  <li><time>2011.02.19.</time>似顔絵売買仲介の「モフルナ」がオープンしました。</li>
  <li><time>2011.02.19.</time>モフルナオープン 似顔絵売買仲介の「モフルナ」がオープン。</li>
</ul>

<aside class="abs side" style="top:145px">
  <div class="side-head">会員登録</div>
  <div style="padding-top:10px">
    <a class="pill" href="#">購入したい方</a>
    <div class="reg"><svg class="ico" viewBox="0 0 46 40"><path d="M2 6h7l5 20h24l4-14H12" fill="none" stroke="#d42a2a" stroke-width="3"/><circle cx="17" cy="33" r="3.5" fill="#555"/><circle cx="34" cy="33" r="3.5" fill="#555"/></svg><span>ユーザー<br>会員登録</span></div>
    <a class="pill" href="#">販売したい方</a>
    <div class="reg"><svg class="ico" viewBox="0 0 46 40"><rect x="8" y="4" width="28" height="26" rx="2" fill="#e9e4dc" stroke="#888"/><ellipse cx="16" cy="32" rx="13" ry="6" fill="#e5a64a"/><circle cx="11" cy="31" r="2" fill="#d22"/><circle cx="18" cy="33" r="2" fill="#27c"/></svg><span>クリエイター<br>会員登録</span></div>
  </div>
</aside>

<aside class="abs side search" style="top:372px">
  <div class="side-head" style="margin-bottom:10px">クリエイター検索</div>
  <div class="row"><span>カテゴリ</span><div class="sel">指定なし</div></div>
  <div class="row"><span>種類</span><div class="chk"><label><i></i>データ</label><label><i></i>現物</label></div></div>
  <div class="row" style="margin-bottom:2px"><span>価格帯</span><div class="sel">下限なし</div></div>
  <div class="row"><span></span><div class="sel">上限なし</div></div>
  <div class="row"><span>納期</span><div class="sel">指定なし</div></div>
  <div class="row"><span style="line-height:1.25">ユーザー<br>評価</span><div class="sel">指定なし</div></div>
  <a class="sbtn" href="#">Q 検索</a>
</aside>

<aside class="abs side" style="top:646px">
  <div class="side-head">商品検索</div>
  <ul class="goods">
    <li><span class="thumb"></span>名刺</li>
    <li><span class="thumb"></span>似顔絵</li>
    <li><span class="thumb"></span>パンフレット</li>
    <li><span class="thumb"></span>ウェルカムボード</li>
    <li><span class="thumb"></span>ロゴデザイン</li>
    <li class="other">その他</li>
  </ul>
</aside>

<div class="abs foot-rule"></div>
<p class="abs foot-links">特定商取引に基づく表示 ｜利用規約｜個人情報保護法｜お問い合わせ</p>
<p class="abs copy">Copyright (C) Mofuruna. All Rights Reserved.</p>

</body>
</html>
```